Brand new leaflet design creative ideas.

I need a flyer designed for my business

I run a pay weekly carpet business and need designs for a flyer this design i will also want to enable it on letterheads business cards and a logo from it when created.

my domain name is www.pebblemarsh.co.uk / www.pebblemarsh.com

Our main competitor i have attached his design to this brief to give you a bit of an idea on how we work, however i do not want a copycat design i want a brand new design something not like theres but eye catching direct to the point.

We are open to colour suggestions as long as the colours work.
Thank you.

Target Market(s)

This print material will be delivered to customers houses.

Industry/Entity Type

Flooring

Font styles to use
Serif
Sans Serif

Requirements
Must have
• Website domain name,
• Various print options CMYK, PDF
Nice to have
• Creativity eye catching
Should not have
• SHOULD NOT BE A COPYCAT DESIGN SOMETHING NEW & CREATIVE

```html
<!DOCTYPE html>
<html lang="en">
<head>
<meta charset="utf-8">
<title>Amazing Carpet Offers from Pebblemarsh</title>
<link rel="stylesheet" href="https://fonts.googleapis.com/css2?family=Jost:ital,wght@0,400;0,500;0,700;1,500&family=Lato:wght@400;700&display=swap">
<style>
  :root {
    --backdrop: #e6e7e9;
    --paper: #f1eee7;
    --paper-edge: #e6e1d6;
    --sky: #2ba2d6;
    --sky-deep: #1c86bd;
    --charcoal: #4a4a4c;
    --flame-top: #f58a2a;
    --flame-bottom: #e5422b;
    --alert: #d8262b;
    --band: #d9252e;
    --ink: #3c3c3c;
    --white: #ffffff;
  }
  * { box-sizing: border-box; margin: 0; padding: 0; }
  html, body { width: 1200px; height: 869px; overflow: hidden; }
  body { background: var(--backdrop); position: relative; font-family: "Lato", sans-serif; }

  .flyer {
    position: absolute; left: 330px; top: 20px; width: 540px; height: 830px;
    background: linear-gradient(180deg, var(--paper) 0%, var(--paper-edge) 100%);
    box-shadow: 0 6px 24px rgba(0,0,0,.18);
    overflow: hidden;
  }

  .headline { position: absolute; top: 26px; left: 0; right: 0; text-align: center; font-family: "Jost", sans-serif; }
  .headline-amazing { color: var(--sky); font-size: 64px; font-weight: 500; letter-spacing: 1px; line-height: 1; }
  .headline-offers { color: var(--charcoal); font-size: 42px; font-weight: 400; line-height: 1; margin-top: 4px; text-shadow: 0 1px 1px rgba(0,0,0,.15); }

  .from-rule { position: absolute; top: 150px; left: 50px; right: 50px; height: 26px; }
  .from-rule::before { content: ""; position: absolute; left: 0; right: 0; top: 12px; border-top: 1.5px solid var(--sky); }
  .from-tag {
    position: absolute; left: 50%; top: 0; transform: translateX(-50%);
    background: var(--sky); color: var(--white); font-family: "Jost", sans-serif;
    font-style: italic; font-weight: 500; font-size: 20px; letter-spacing: 1px;
    padding: 0 18px; line-height: 26px;
  }

  .brand-name {
    position: absolute; top: 180px; left: 0; right: 0; text-align: center;
    font-family: "Jost", sans-serif; font-weight: 700; font-size: 66px; letter-spacing: 1px; line-height: 1.1;
    color: var(--flame-bottom);
    background: linear-gradient(180deg, var(--flame-top), var(--flame-bottom));
    -webkit-background-clip: text; background-clip: text; -webkit-text-fill-color: transparent;
  }

  .perks { position: absolute; top: 340px; left: 40px; list-style: none; font-size: 19px; color: var(--ink); line-height: 30px; }
  .perks li::before { content: "•"; margin-right: 8px; }
  .perks .perk-urgent { color: var(--alert); font-weight: 700; }

  .price-burst { position: absolute; top: 318px; left: 316px; width: 200px; height: 200px; }
  .price-burst svg { position: absolute; inset: 0; }
  .price-burst-text {
    position: absolute; inset: 0; display: flex; flex-direction: column; align-items: center; justify-content: center;
    color: var(--white); font-family: "Jost", sans-serif; line-height: 1.05; text-align: center;
  }
  .price-burst-text .small { font-size: 22px; font-weight: 400; }
  .price-burst-text .amount { font-size: 36px; font-weight: 700; }

  .family-photo {
    position: absolute; top: 552px; left: 0; right: 0; height: 214px;
    background: linear-gradient(180deg, #e9e3d2 0%, #d9d1bd 45%, #f4f2ec 100%);
  }

  .visit-label { position: absolute; top: 772px; left: 0; right: 0; text-align: center; font-size: 12px; color: var(--ink); letter-spacing: .5px; }
  .web-band {
    position: absolute; top: 790px; left: 0; right: 0; height: 32px; background: var(--band);
    display: flex; align-items: center; justify-content: center; gap: 16px;
    color: var(--white); font-size: 14px;
  }
</style>
</head>
<body>
  <main class="flyer">
    <header class="headline">
      <div class="headline-amazing">AMAZING</div>
      <div class="headline-offers">CARPET OFFERS</div>
    </header>

    <div class="from-rule"><span class="from-tag">FROM</span></div>
    <h1 class="brand-name">PEBBLEMARSH</h1>

    <ul class="perks">
      <li>No Credit Checks</li>
      <li>Free Home measuring</li>
      <li>Free Underlay</li>
      <li>Free Grippers</li>
      <li>Free Door Trims</li>
      <li class="perk-urgent">Dont delay!</li>
    </ul>

    <div class="price-burst">
      <svg viewBox="0 0 200 200" width="200" height="200" aria-hidden="true">
        <polygon fill="var(--sky-deep)" points="200,100 185,122.8 186.6,150 162.2,162.2 150,186.6 122.8,185 100,200 77.2,185 50,186.6 37.8,162.2 13.4,150 15,122.8 0,100 15,77.2 13.4,50 37.8,37.8 50,13.4 77.2,15 100,0 122.8,15 150,13.4 162.2,37.8 186.6,50 185,77.2"/>
      </svg>
      <div class="price-burst-text">
        <span class="small">Pay only</span>
        <span class="amount">$10.00</span>
        <span class="small">per week</span>
      </div>
    </div>

    <div class="family-photo" role="img" aria-label="Photo of two smiling children lying on a soft cream carpet with laptops"></div>

    <footer>
      <div class="visit-label">VISIT US AT</div>
      <div class="web-band">
        <span>www.pebblemarsh.co.uk</span><span>|</span><span>www.pebblemarsh.com</span>
      </div>
    </footer>
  </main>
</body>
</html>
```